Financial Services Business Card Design

We are a financial services company Based in London, offering Short term Funding Solutions for companies, raising anywhere between £20,000 and £25million pounds.

The Card must have a professional look as it is going to be handed out to professionals I.E Solicitors, Accountants, Company directors and Business owners.

See Attached our company Logo

Industry/Entity Type

Business

Contact Information for Business Card

Lewis Thorncroft
Suite 41
R K House
Bramblecote Lane
Watford
HP19 4QX

```html
<!DOCTYPE html>
<html lang="en">
<head>
<meta charset="utf-8">
<title>Kestrel Bridge Finance – Business Card</title>
<link href="https://fonts.googleapis.com/css2?family=Open+Sans:wght@400;600;700&display=swap" rel="stylesheet">
<style>
  :root {
    --brand-blue: #2171b9;
    --brand-green: #3aa94a;
    --ink: #1c1c1c;
    --paper: #ffffff;
    --backdrop: #e8e5e1;
  }
  * { margin: 0; padding: 0; box-sizing: border-box; }
  html, body { width: 1200px; height: 1000px; overflow: hidden; }
  body {
    background: var(--backdrop);
    font-family: "Open Sans", Arial, sans-serif;
    position: relative;
  }
  .card {
    position: absolute;
    left: 265px;
    width: 666px;
    height: 397px;
    overflow: hidden;
    box-shadow: 0 4px 10px rgba(0,0,0,.25);
  }
  .card--front { top: 73px; background: var(--paper); }
  .card--back { top: 532px; background: var(--brand-blue); }

  .brand {
    position: absolute;
    display: flex;
    align-items: center;
    gap: 12px;
    font-weight: 700;
    white-space: nowrap;
  }
  .brand__dot { width: 18px; height: 18px; border-radius: 50%; flex: none; }
  .card--front .brand { left: 32px; top: 130px; color: var(--brand-blue); font-size: 31px; }
  .card--front .brand__dot { background: var(--brand-blue); }
  .card--back .brand { left: 0; right: 0; top: 178px; justify-content: center; color: #fff; font-size: 40px; }
  .card--back .brand__dot { background: #fff; width: 22px; height: 22px; }

  .holder {
    position: absolute;
    right: 32px;
    top: 214px;
    color: var(--brand-blue);
    font-size: 22px;
    font-weight: 600;
  }
  .rule {
    position: absolute;
    left: 32px; right: 32px; top: 249px;
    border-top: 2px solid var(--ink);
  }
  .address {
    position: absolute;
    left: 32px; top: 273px;
    font-style: normal;
    font-size: 16px;
    line-height: 24px;
    color: var(--ink);
  }
  .contacts {
    position: absolute;
    right: 32px; top: 273px;
    list-style: none;
    font-size: 16px;
    line-height: 24px;
    color: var(--ink);
    text-align: right;
  }
  .contacts li { display: flex; justify-content: flex-end; align-items: center; gap: 8px; }
  .contacts svg { width: 16px; height: 14px; fill: var(--brand-blue); }

  .footer-wave { position: absolute; left: 0; bottom: 0; width: 666px; height: 60px; }
  .website {
    position: absolute;
    left: 0; right: 0;
    color: #fff;
    font-size: 16px;
    letter-spacing: 1px;
    text-align: center;
  }
  .card--front .website { bottom: 6px; }
  .card--back .website { bottom: 27px; }
</style>
</head>
<body>

<section class="card card--front">
  <div class="brand"><span class="brand__dot"></span>Kestrel Bridge Finance</div>
  <div class="holder">Lewis Thorncroft</div>
  <div class="rule"></div>
  <address class="address">
    Suite 41 R K House<br>
    Bramblecote Lane<br>
    Watford HP19 4QX
  </address>
  <ul class="contacts">
    <li>+ 000 000 0000
      <svg viewBox="0 0 16 14"><path d="M1 5c0-2 3-3 7-3s7 1 7 3v1h-3V4.5H4V6H1z"/><rect x="3" y="7" width="10" height="6" rx="1"/></svg>
    </li>
    <li>+ 000 000 0000
      <svg viewBox="0 0 16 14"><rect x="4" y="0" width="8" height="4"/><rect x="0" y="4" width="16" height="6" rx="1"/><rect x="4" y="8" width="8" height="6"/></svg>
    </li>
    <li>info@kestrelbridge.com
      <svg viewBox="0 0 16 14"><path d="M0 2h16v1L8 8 0 3z"/><path d="M0 5l8 5 8-5v8H0z"/></svg>
    </li>
  </ul>
  <svg class="footer-wave" viewBox="0 0 666 60" preserveAspectRatio="none">
    <path d="M60 19 Q333 -4 610 20 Q333 6 60 19z" fill="var(--brand-green)"/>
    <path d="M0 44 Q333 2 666 44 V60 H0z" fill="var(--brand-blue)"/>
  </svg>
  <div class="website">www.kestrelbridge.com</div>
</section>

<section class="card card--back">
  <div class="brand"><span class="brand__dot"></span>Kestrel Bridge Finance</div>
  <div class="website">www.kestrelbridge.com</div>
</section>

</body>
</html>
```